New business logo / Business Card Design

My company provides Interim Management and consultancy, for Facilities Services. Covers any aspect of facilities management, including M&E, helpdesk, asset management, supplier relationships, catering, cleaning etc. Company provides innovative solutions to exceed client needs, drawing on years of experience. Initial thoughts on logo are attached below. Fits with RAG status on projects, red, amber and green, with logo design colours around moving services from amber to green.

Target Market(s)

Facilities Management clients and service providers

Industry/Entity Type

Business

Contact Information for Business Card

Company Name = k7Rventures Ltd My name on card = Derek Haskins, Director Mobile = 07912365048 Email = Derek@k7rventuresltd.co.uk Twitter = @k7Rventures Ltd

Font styles to use
Sans Serif

Colors
f37122
00a990

Requirements
Must have
• Logo to be evident, with some background image in reference to Facilities Management

```html
<!DOCTYPE html>
<html lang="en">
<head>
<meta charset="utf-8">
<title>k7Rventures Ltd – Business Card</title>
<link href="https://fonts.googleapis.com/css2?family=Didact+Gothic&family=Open+Sans:wght@400;700&display=swap" rel="stylesheet">
<style>
  :root {
    --bg: #e9e7e4;
    --paper: #ffffff;
    --charcoal: #2a2a2a;
    --charcoal-light: #363636;
    --green: #146b3a;
    --orange: #f26822;
    --ink: #222222;
    --muted: #8a8a8a;
    --white: #ffffff;
  }
  * { margin: 0; padding: 0; box-sizing: border-box; }
  html, body { width: 1200px; height: 900px; overflow: hidden; background: var(--bg); }
  .canvas { position: relative; width: 1200px; height: 900px; }

  .card {
    position: absolute; left: 285px; width: 630px; height: 360px;
    box-shadow: 0 6px 18px rgba(0,0,0,.18); overflow: hidden;
  }
  .card--front { top: 70px; background: var(--paper); }
  .card--back {
    top: 470px;
    background: radial-gradient(circle at 55% 45%, var(--charcoal-light), var(--charcoal) 70%);
  }

  .card__shapes { position: absolute; inset: 0; }

  .holder { position: absolute; left: 72px; top: 26px; font-family: "Open Sans", sans-serif; }
  .holder__name { font-weight: 700; font-size: 19px; color: var(--green); line-height: 1.1; }
  .holder__surname { color: var(--orange); }
  .holder__role { font-size: 12px; color: var(--green); }

  .contact { position: absolute; left: 36px; top: 178px; list-style: none;
    font-family: "Open Sans", sans-serif; font-size: 13.5px; color: var(--green); }
  .contact__item { display: flex; align-items: center; gap: 9px; height: 21px; }
  .contact__icon { width: 11px; height: 11px; flex: none; }

  .brand { position: absolute; left: 355px; top: 150px; display: flex; flex-direction: column; align-items: center; gap: 12px; }
  .brand__dot { width: 72px; height: 72px; border-radius: 50%; background: var(--green); border: 4px solid #d0d0d0; }
  .brand__name { font-family: "Didact Gothic", sans-serif; font-size: 27px; color: var(--ink); letter-spacing: .5px; }

  .back__ring { position: absolute; left: 205px; top: 70px; width: 220px; height: 220px;
    border-radius: 50%; border: 10px solid rgba(255,255,255,.05); }
  .back__name { position: absolute; inset: 0; display: flex; align-items: center; justify-content: center;
    font-family: "Didact Gothic", sans-serif; font-size: 44px; color: var(--white); letter-spacing: 1px; }
</style>
</head>
<body>
<main class="canvas">

  <section class="card card--front" aria-label="Business card front">
    <svg class="card__shapes" width="630" height="360" viewBox="0 0 630 360" aria-hidden="true">
      <polygon points="0,0 46,0 0,46" fill="var(--green)"/>
      <polygon points="46,0 56,0 56,46 8,46" fill="var(--orange)"/>
      <polygon points="0,262 218,262 204,290 0,290" fill="var(--green)"/>
      <polygon points="226,296 630,296 630,336 206,336" fill="var(--orange)"/>
    </svg>

    <div class="holder">
      <p class="holder__name">Derek <span class="holder__surname">Haskins</span></p>
      <p class="holder__role">Director</p>
    </div>

    <ul class="contact">
      <li class="contact__item">
        <svg class="contact__icon" viewBox="0 0 11 11"><rect x="2.5" y="0.5" width="6" height="10" rx="1.2" fill="none" stroke="var(--orange)" stroke-width="1.3"/><circle cx="5.5" cy="8.5" r=".8" fill="var(--orange)"/></svg>
        07912365048
      </li>
      <li class="contact__item">
        <svg class="contact__icon" viewBox="0 0 11 11"><rect x="0" y="2" width="11" height="7.5" fill="var(--orange)"/><polyline points="0.5,2.5 5.5,6.5 10.5,2.5" fill="none" stroke="var(--white)" stroke-width="1"/></svg>
        Derek@k7rventuresltd.co.uk
      </li>
      <li class="contact__item">
        <svg class="contact__icon" viewBox="0 0 11 11"><rect width="11" height="11" rx="1.5" fill="var(--orange)"/></svg>
        @k7Rventures Ltd
      </li>
    </ul>

    <div class="brand">
      <span class="brand__dot" aria-hidden="true"></span>
      <p class="brand__name">k7Rventures Ltd</p>
    </div>
  </section>

  <section class="card card--back" aria-label="Business card back">
    <span class="back__ring" aria-hidden="true"></span>
    <p class="back__name">k7Rventures Ltd</p>
  </section>

</main>
</body>
</html>
```